Brisk. Technology Logistics Software platform.

A modern looking and feeling website for a logistics software platform.
We connect retailers or wholesale parcel distributors to worldwide delivery solutions.
Methods tend to be road and air transport to final mile courier companies and post offices all over the world.
Our platform is for ecommerce distribution. A customer uses BRISK to enable them to connect to worldwide companies who will track and trace the delivery of their goods.

Target Market(s)

Onllne retailers. Markert Places such as Vorlix and Quendro. Wholesale third party logistics and packaging companies. Delivery companies based in the UK looking to expand overseas.

Number of Pages Required

5+ page

Font styles to use
Sans Serif

Colors
aaaaaa
dbdbdb
e6e6e6
c4c4c4
cbcbcb
c9c9c9
ec1f27
3176b5
0355a3

Requirements
Must have
• Landing Page.
• What we do.
• Who we are.
• Modules.
• Testimonies (password protected)
• Contact us.
• Interactive for mobile operating systems.
• Scrolling website.
• Short stock video showing on key pages.
• Very well polished fonts and buttons. A sharp and well executed website is required.
• Simplicity in feeling.
• To the point on message.
• Refined wording and copyrighting / messaging
• A link to our sub brand and product Brisk Parcels
• Capture interest so people read further.
Nice to have
• A polished video to explain what we do on landing page. Clipmarrow.net have some good options but not sure how professional they will look.
Should not have
• Bad graphics and colours.
• Not lots of clicks. Less as possible
• Complex message

```html
<!DOCTYPE html>
<html lang="en">
<head>
<meta charset="utf-8">
<title>Brisk. Technology – Website</title>
<link rel="stylesheet" href="https://fonts.googleapis.com/css2?family=Roboto:wght@500;700&family=Open+Sans:wght@400;600&display=swap">
<style>
:root{
  --stage:#ebebeb;
  --white:#ffffff;
  --red:#ec1f27;
  --ink:#222222;
  --body-grey:#666666;
  --footer:#0b0b0b;
  --hero-dark:#3a3430;
  --hero-blue:#3176b5;
  --hero-yellow:#a88f2c;
}
*{margin:0;padding:0;box-sizing:border-box}
html,body{width:1200px;height:703px;overflow:hidden;background:var(--stage)}
body{position:relative;font-family:"Open Sans",Arial,sans-serif}
.screen{position:absolute;width:460px;background:var(--white);box-shadow:0 3px 10px rgba(0,0,0,.18);overflow:hidden}
.screen--mobile{left:96px;top:110px;height:289px}
.screen--desktop{left:644px;top:110px;height:483px}
.site-header{position:absolute;left:0;top:0;width:460px;height:38px;background:var(--white)}
.brand{position:absolute;left:43px;top:10px;display:flex;align-items:center;gap:5px;font-family:"Roboto",Arial,sans-serif;font-weight:700;font-size:15px;color:var(--red);letter-spacing:-.2px}
.brand-dot{width:9px;height:9px;border-radius:50%;background:var(--red)}
.menu-toggle{position:absolute;left:400px;top:11px;width:18px;height:18px;border:1px solid #555;border-radius:50%}
.menu-toggle svg{position:absolute;left:4px;top:5px}
.main-nav{position:absolute;right:42px;top:15px;display:flex;gap:15px;font-family:"Roboto",Arial,sans-serif;font-weight:500;font-size:6px;color:var(--ink);align-items:center}
.main-nav .is-active{color:var(--red)}
.hero{position:absolute;left:0;top:38px;width:460px;height:222px}
.hero-photo{position:absolute;inset:0;background:
  linear-gradient(90deg,rgba(49,118,181,.35) 0%,rgba(0,0,0,0) 30%,rgba(0,0,0,0) 70%,rgba(49,118,181,.35) 100%),
  linear-gradient(160deg,#5a5550 0%,var(--hero-dark) 45%,#4a403a 70%,#2f2b28 100%)}
.hero-photo::after{content:"";position:absolute;inset:0;background:linear-gradient(100deg,transparent 30%,rgba(168,143,44,.25) 38%,transparent 46%,transparent 78%,rgba(168,143,44,.22) 84%,transparent 90%)}
.hero-title{position:absolute;left:0;width:100%;text-align:center;font-family:"Roboto",Arial,sans-serif;font-weight:700;color:var(--white)}
.screen--mobile .hero-title{top:38px;font-size:26px}
.screen--desktop .hero-title{top:42px;font-size:20.5px;line-height:29px}
.hero-lead{position:absolute;left:78px;width:304px;top:82px;text-align:center;color:var(--white);font-size:7px;line-height:12.8px}
.slide-arrow{position:absolute;top:102px;width:13px;height:18px;background:rgba(20,20,20,.55);display:flex;align-items:center;justify-content:center}
.slide-arrow--prev{left:0}
.slide-arrow--next{right:0}
.play-button{position:absolute;left:218px;top:151px;width:24px;height:24px;border:1.5px solid var(--white);border-radius:50%}
.play-button svg{position:absolute;left:8px;top:6px}
.intro{position:absolute;left:0;top:260px;width:460px;text-align:center}
.intro-text{margin:30px auto 0;width:302px;font-size:6.4px;line-height:12.2px;color:var(--body-grey)}
.intro-tagline{margin-top:15px;font-size:8.4px;font-weight:600;color:#333}
.cta-row{margin-top:17px;display:flex;justify-content:center;gap:7px}
.cta{width:85px;height:24px;border:1px solid var(--red);border-radius:12px;display:flex;align-items:center;justify-content:center;font-size:6.4px;font-weight:600;color:var(--red)}
.site-footer{position:absolute;left:0;width:460px;height:29px;background:var(--footer);color:var(--white);text-align:center;font-size:5.6px}
.screen--mobile .site-footer{top:260px}
.screen--desktop .site-footer{top:450px;height:33px}
.site-footer p{padding-top:11px}
</style>
</head>
<body>

<section class="screen screen--mobile">
  <header class="site-header">
    <div class="brand"><span class="brand-dot"></span>Brisk. Technology</div>
    <div class="menu-toggle"><svg width="9" height="7" viewBox="0 0 9 7"><path d="M0 .5h9M0 3.5h9M0 6.5h9" stroke="#333" stroke-width="1"/></svg></div>
  </header>
  <div class="hero">
    <div class="hero-photo" role="img" aria-label="Aerial video still of a logistics warehouse with lorries at loading bays"></div>
    <h1 class="hero-title">Brisk.Technology … Our Focus</h1>
    <p class="hero-lead">We provide advanced software solutions to ensure you connect with global ecommerce delivery carriers You can manage your Global Delivery Network in one place, with Our software will enable you monitor the productivity and reporting of your ecommerce deliveries Manage your carriers, your delivery speeds, and your costs</p>
    <div class="slide-arrow slide-arrow--prev"><svg width="6" height="9"><path d="M5 .5 1 4.5 5 8.5" stroke="#fff" fill="none"/></svg></div>
    <div class="slide-arrow slide-arrow--next"><svg width="6" height="9"><path d="M1 .5 5 4.5 1 8.5" stroke="#fff" fill="none"/></svg></div>
    <div class="play-button"><svg width="9" height="10"><path d="M0 0 9 5 0 10Z" fill="#fff"/></svg></div>
  </div>
  <footer class="site-footer"><p>Brisk Technology © 2018 All rights reserved.</p></footer>
</section>

<section class="screen screen--desktop">
  <header class="site-header">
    <div class="brand"><span class="brand-dot"></span>Brisk. Technology</div>
    <nav class="main-nav">
      <span class="is-active">HOME</span><span>SOLUTIONS</span><span>TESTIMONIAL LOGIN</span><span>CONTACT US</span>
      <svg width="7" height="7" viewBox="0 0 7 7"><circle cx="3" cy="3" r="2.2" stroke="#222" stroke-width="1.1" fill="none"/><path d="M4.6 4.6 6.6 6.6" stroke="#222" stroke-width="1.2"/></svg>
    </nav>
  </header>
  <div class="hero">
    <div class="hero-photo" role="img" aria-label="Aerial video still of a logistics warehouse with lorries at loading bays"></div>
    <h1 class="hero-title">Brisk. Technology and Parcel Solutions<br>Built To Help Develop &amp; Manage<br>Your Global Delivery Network</h1>
    <div class="slide-arrow slide-arrow--prev"><svg width="6" height="9"><path d="M5 .5 1 4.5 5 8.5" stroke="#fff" fill="none"/></svg></div>
    <div class="slide-arrow slide-arrow--next"><svg width="6" height="9"><path d="M1 .5 5 4.5 1 8.5" stroke="#fff" fill="none"/></svg></div>
    <div class="play-button"><svg width="9" height="10"><path d="M0 0 9 5 0 10Z" fill="#fff"/></svg></div>
  </div>
  <div class="intro">
    <p class="intro-text">Working closely with Ecommerce, Brisk. Technology have developed solutions purely focused on delivering what’s required within the global delivery marketplace. Meeting all needs and more for Retailers and Global Delivery Solution providers Allowing customers to grow at a fast pace; most importantly providing tools to help them manage their global delivery network supported by “Dynamic Real Time Visibility” management tools</p>
    <p class="intro-tagline">Ensuring solutions evolve to suit our customers business requirements</p>
    <div class="cta-row"><span class="cta">BRISK PARCEL</span><span class="cta">BRISK TECHNIOLOGY</span></div>
  </div>
  <footer class="site-footer"><p>Brisk Technology © 2018 All rights reserved.</p></footer>
</section>

</body>
</html>
```